Design for new site

Hi, we need a web design for a new product calmridgeway.
This product is aimed to help people with anxiety, panic attacks and other disorders on permanently basis.
Please take a look at competitors web-sites:
http://www.brightharborpath.example/
http://www.stillmeadow.example/
Key Audiences
The intended audience for this site will be people that are looking for relief from panic and anxiety.
Key Objectives
Key object is to get prospective clients to sign up for membership and purchase our audio course.
Theme of Site
The general site theme needs to be clean and simple. The audience coming to the site in under a lot of anxiety and we don’t want to add any stress.
The site needs to flow easy from top down, with few distractions in side menus and/or columns.
Color Scheme
Suggested colors need to be light shades of blue. Blue psychology is tranquil, peaceful, and calm. This color has a tremendous stress management quality to it, making us feel cool and calm.
Or it can be shades of cool green of summer forest.
Please take a look at site mock up in attachment.

```html
<!DOCTYPE html>
<html lang="en">
<head>
<meta charset="utf-8">
<title>Calmridge Way</title>
<link href="https://fonts.googleapis.com/css2?family=Titillium+Web:wght@400;600;700&family=Open+Sans:ital,wght@0,400;0,600;0,700;1,600&display=swap" rel="stylesheet">
<style>
  :root {
    --sky: #33c9fb;
    --sky-deep: #22b4ea;
    --ink: #1d1d1d;
    --body: #555;
    --white: #fff;
    --footer: #1b1b1b;
    --footer-text: #e6e6e6;
  }
  * { margin: 0; padding: 0; box-sizing: border-box; }
  html, body { width: 938px; height: 1200px; overflow: hidden; background: var(--white); }
  body { position: relative; font-family: "Open Sans", sans-serif; color: var(--body); }

  .site-header { position: absolute; top: 0; left: 0; width: 938px; height: 88px; background: var(--sky); }
  .brand { position: absolute; left: 76px; top: 26px; font-family: "Titillium Web", sans-serif; font-weight: 600; font-size: 24px; color: var(--white); }
  .main-nav { position: absolute; right: 78px; top: 37px; display: flex; gap: 19px; }
  .main-nav a { font-size: 10px; font-weight: 600; color: var(--ink); text-decoration: none; }

  .hero { position: absolute; top: 88px; left: 0; width: 938px; height: 316px;
    background: linear-gradient(100deg, #3d5d86 0%, #4a7a9a 25%, #5ea39a 45%, #78bcc9 65%, #4970a4 85%, #3c5a92 100%); }
  .hero-photo { position: absolute; inset: 0; background: radial-gradient(circle at 30% 75%, rgba(90,170,110,.55), transparent 35%), radial-gradient(circle at 60% 65%, rgba(140,220,235,.5), transparent 40%); }
  .hero-icon { position: absolute; left: 429px; top: 62px; width: 80px; height: 80px; border-radius: 50%; background: var(--sky); }
  .hero-icon svg { position: absolute; left: 20px; top: 18px; }
  .hero-title { position: absolute; top: 155px; width: 100%; text-align: center; font-family: "Titillium Web", sans-serif; font-weight: 600; font-size: 23px; color: var(--white); }
  .hero-sub { position: absolute; top: 198px; width: 100%; text-align: center; font-family: "Titillium Web", sans-serif; font-weight: 600; font-size: 12.5px; color: var(--white); }
  .hero-dots { position: absolute; top: 290px; left: 442px; display: flex; gap: 7px; }
  .hero-dots span { width: 10px; height: 10px; border-radius: 50%; border: 1.5px solid #555; background: var(--white); }
  .hero-dots span.active { background: var(--sky); border-color: #2b8cc0; }

  .section-title { font-family: "Titillium Web", sans-serif; font-weight: 600; font-size: 23px; color: var(--sky); }
  .copy { font-size: 10.4px; line-height: 18.8px; }

  .welcome { position: absolute; top: 420px; left: 76px; width: 784px; text-align: center; }
  .welcome .copy { margin-top: 3px; }

  .stories { position: absolute; top: 585px; left: 76px; width: 470px; }
  .stories .copy { margin-top: 4px; padding-left: 2px; }
  .stories-visual { position: absolute; left: 588px; top: 570px; width: 270px; height: 226px; }
  .screen { position: absolute; left: 0; top: 0; width: 270px; height: 180px; border-radius: 5px; background: #111; }
  .screen-fill { position: absolute; left: 12px; top: 12px; width: 246px; height: 163px; background: linear-gradient(180deg, #eef1f6 0%, #7f8fc6 18%, #a57bbd 45%, #f4f4f6 60%, #ffffff 100%); }
  .stand { position: absolute; left: 98px; top: 180px; width: 76px; height: 46px; background: linear-gradient(90deg, #9a9a9a, #eeeeee 50%, #9a9a9a); clip-path: polygon(18% 0, 82% 0, 90% 92%, 100% 100%, 0 100%, 10% 92%); }

  .partners { position: absolute; top: 844px; left: 0; width: 938px; height: 112px; background: var(--sky); display: flex; align-items: center; justify-content: center; gap: 50px; }
  .partner { display: flex; align-items: center; gap: 8px; font-family: "Open Sans", sans-serif; font-weight: 700; font-size: 20px; color: var(--white); }
  .partner i { width: 22px; height: 22px; background: var(--white); border-radius: 50%; }
  .partner i.sq { border-radius: 0; }

  .testimonials { position: absolute; top: 986px; left: 79px; }
  .quote { position: absolute; top: 1040px; width: 360px; }
  .quote.left { left: 93px; }
  .quote.right { left: 495px; }
  .quote p { font-size: 10.2px; line-height: 18.8px; color: #444; }
  .quote cite { display: block; text-align: right; font-style: italic; font-weight: 600; font-size: 9.5px; color: var(--ink); margin-top: 2px; padding-right: 11px; }
  .mark { position: absolute; font-family: Georgia, serif; font-size: 30px; line-height: 1; color: #666; }
  .mark.open { left: -17px; top: -9px; }
  .mark.close { right: -12px; bottom: -20px; }

  .site-footer { position: absolute; top: 1118px; left: 0; width: 938px; height: 82px; background: var(--footer); }
  .footer-links { position: absolute; left: 77px; top: 23px; font-size: 9.5px; color: var(--footer-text); }
  .footer-links a { color: var(--footer-text); text-decoration: none; }
  .footer-links span { margin: 0 5px; }
  .copyright { position: absolute; left: 77px; top: 42px; font-size: 9.5px; color: var(--footer-text); }
  .social { position: absolute; left: 765px; top: 35px; display: flex; gap: 7px; }
  .social span { width: 19px; height: 19px; border-radius: 3px; background: #3c6fa8; }
  .social span:nth-child(2) { background: #4cbbe8; }
  .social span:nth-child(3) { background: #2a7ab4; }
  .social span:nth-child(4) { background: #e8821e; }
</style>
</head>
<body>
  <header class="site-header">
    <div class="brand">Calmridge Way</div>
    <nav class="main-nav">
      <a href="#">Home</a><a href="#">Product</a><a href="#">Success</a><a href="#">Stories</a><a href="#">Anxiety</a><a href="#">Test</a><a href="#">Blog</a><a href="#">About</a><a href="#">FAQ</a><a href="#">Contact Us</a>
    </nav>
  </header>

  <section class="hero">
    <div class="hero-photo" role="img" aria-label="Soft blurred background photo in blue and green tones"></div>
    <div class="hero-icon">
      <svg width="40" height="44" viewBox="0 0 40 44" fill="none" stroke="#fff" stroke-width="1.6" stroke-linecap="round">
        <path d="M14 28c0-4-5-6-5-13a11 11 0 0 1 22 0c0 7-5 9-5 13z"/>
        <path d="M15 31h10M15 34h10M17 37h6"/>
        <path d="M20 0v4M4 6l3 3M36 6l-3 3M0 18h4M36 18h4M3 29l3-2M37 29l-3-2"/>
      </svg>
    </div>
    <h1 class="hero-title">Lorem ipsum dolor sit amet, consectetuer adipiscing elit</h1>
    <p class="hero-sub">Lorem ipsum dolor sit amet, consectetuer adipiscing elit, sed diam nonummy nibh euismod tincidunt ut laoreet</p>
    <div class="hero-dots"><span class="active"></span><span></span><span></span></div>
  </section>

  <section class="welcome">
    <h2 class="section-title">Welcome To Calmridge Way</h2>
    <p class="copy">Lorem ipsum dolor sit amet, consectetuer adipiscing elit, sed diam nonummy nibh euismod tincidunt ut laoreet dolore magna aliquam erat volutpat. Ut wisi enim ad minim veniam, quis nostrud exerci tation ullamcorper suscipit lobortis nisl ut aliquip ex ea commodo consequat Lorem ipsum dolor sit amet, consectetuer adipiscing elit, sed diam nonummy nibh euismod tincidunt ut laoreet dolore magna aliquam erat volutpat. Ut wisi enim ad minim veniam, quis nostrud exerci tation ullamcorper suscipit lobortis nisl ut aliquip ex ea commodo consequat</p>
  </section>

  <section class="stories">
    <h2 class="section-title">Still Meadow Success Stories</h2>
    <p class="copy">Lorem ipsum dolor sit amet, consectetuer adipiscing elit, sed diam nonummy nibh euismod tincidunt ut laoreet dolore magna aliquam erat volutpat. Ut wisi enim ad minim veniam, quis nostrud exerci tation ullamcorper suscipit lobortis nisl ut aliquip ex ea commodo consequat Lorem ipsum dolor sit amet, consectetuer adipiscing elit, sed diam nonummy nibh euismod tincidunt ut laoreet dolore magna aliquam erat volutpat. Ut wisi enim ad minim veniam, quis nostrud exerci tation ullamcorper suscipit lobortis nisl ut aliquip ex ea commodo consequat</p>
  </section>
  <div class="stories-visual">
    <div class="screen"><div class="screen-fill" role="img" aria-label="Website preview shown on a desktop monitor"></div></div>
    <div class="stand"></div>
  </div>

  <section class="partners">
    <div class="partner"><i></i>Openfield Net</div>
    <div class="partner"><i class="sq"></i>Relay Works</div>
    <div class="partner"><i></i>Buildnest</div>
    <div class="partner">Sitefolio</div>
  </section>

  <h2 class="section-title testimonials">Testimonials</h2>
  <blockquote class="quote left">
    <span class="mark open">&ldquo;</span>
    <p>Lorem ipsum dolor sit amet, consectetuer adipiscing elit. Aenean commodo ligula eget dolor. Aenean massa. Cum sociis natoque penatibus et</p>
    <cite>-Aaron Pell, CEO</cite>
    <span class="mark close">&rdquo;</span>
  </blockquote>
  <blockquote class="quote right">
    <span class="mark open">&ldquo;</span>
    <p>Lorem ipsum dolor sit amet, consectetuer adipiscing elit. Aenean commodo ligula eget dolor. Aenean massa. Cum sociis natoque penatibus et</p>
    <cite>-Aaron Pell, CEO</cite>
    <span class="mark close">&rdquo;</span>
  </blockquote>

  <footer class="site-footer">
    <div class="footer-links"><a href="#">Home</a><span>|</span><a href="#">About Us</a><span>|</span><a href="#">Products</a><span>|</span><a href="#">Contact Us</a></div>
    <div class="copyright">&copy; 2014 Company Name &nbsp;All right reserved &nbsp;Term of Use</div>
    <div class="social" role="img" aria-label="Social media links"><span></span><span></span><span></span><span></span></div>
  </footer>
</body>
</html>
```